依頼詳細
12月の年末繁忙期に合わせて、新聞折込を実施する予定です。ただ、おコメの麺の説明が難しく消費者には伝わりにくいため、純粋にちゃんぽんや台湾風まぜそばを全面に打ち出して当社に来店してもらい、結果的に米粉麺だったくらいの主張でいいと思っています。チラシの下部に100円キャッシュバック券をつけたいと考えています。(期限は2023年2月末)
記載項目
こむぎ茶屋 しずくや みずほ灯籠館店 (道の駅みずほ灯籠館内フードコート)
住所 長岡市桜井町318 TEL090-6978-5739
営業時間10:00~19:00

とろみちゃんぽん 880円
とろみちゃんぽん旨辛味噌のせ 910円
台湾風まぜそば 910円
サイズ
A4
ページ数
片面
希望イメージ
シンプル 複雑
単色 カラフル
暗い 明るい
日常 高級
遊び心 厳粛
未来的 伝統的
女性的 男性的
希望する色
黄・オレンジ系
納品ファイル
• 高解像度JPG (.jpg)

はじめてみた人が感じるインパクトがあり、色彩もよかったです。

毎回たくさんの応募ありがとうございます。
結果的に非常に満足しておりますので、これからも依頼したいと思います。
よろしくお願いします。

```html
<!DOCTYPE html>
<html lang="ja">
<head>
<meta charset="utf-8">
<title>こむぎ茶屋 しずくや チラシ</title>
<link rel="stylesheet" href="https://fonts.googleapis.com/css2?family=Shippori+Mincho+B1:wght@600;800&family=Noto+Sans+JP:wght@500;700;900&display=swap">
<style>
  :root {
    --navy: #1d2746;
    --navy-deep: #141b33;
    --gold: #f0b323;
    --gold-light: #f6d67a;
    --red: #e2412a;
    --ink: #1a1a1a;
    --white: #ffffff;
    --paper: #fbfaf6;
  }
  * { margin: 0; padding: 0; box-sizing: border-box; }
  html, body { width: 849px; height: 1200px; overflow: hidden; background: var(--white); }
  .flyer {
    position: relative; width: 849px; height: 1200px; overflow: hidden;
    background: var(--paper);
    font-family: "Shippori Mincho B1", serif;
    color: var(--ink);
  }
  .backdrop { position: absolute; inset: 0; }

  .dish {
    position: absolute; border-radius: 50%;
    border: 7px solid var(--navy-deep);
    box-shadow: 0 6px 14px rgba(0,0,0,.25);
  }
  .dish--miso { left: 12px; top: 12px; width: 250px; height: 250px;
    background: radial-gradient(circle at 45% 45%, #f3ece0 0%, #e6c8a0 45%, #b46a3a 75%, #3a2a22 100%); }
  .dish--plain { left: 18px; top: 280px; width: 265px; height: 265px;
    background: radial-gradient(circle at 50% 50%, #f6f1e7 0%, #ecdcc2 50%, #c9a77c 78%, #2d2623 100%); }
  .dish--mazesoba { left: 20px; top: 640px; width: 255px; height: 255px;
    background: radial-gradient(circle at 50% 45%, #c0622c 0%, #8c4a26 30%, #6e8a3c 55%, #d8b66a 72%, #1c1a1a 100%); }

  .menu-label {
    position: absolute; font-family: "Noto Sans JP", sans-serif; font-weight: 700;
    color: var(--ink); line-height: 1.25; white-space: nowrap;
  }
  .menu-label .name { font-size: 22px; display: block; }
  .menu-label .price { font-size: 24px; display: block; font-weight: 500; margin-top: 6px; }
  .label-miso { left: 275px; top: 28px; }
  .label-miso .price { margin-left: 70px; }
  .label-plain { left: 30px; top: 556px; }
  .label-plain .price { margin-left: 90px; margin-top: 0; }
  .label-mazesoba { left: 610px; top: 760px; color: var(--white); }
  .label-mazesoba .price { margin-left: 70px; }

  .v {
    position: absolute; writing-mode: vertical-rl; text-orientation: upright;
    line-height: 1; white-space: nowrap;
  }
  .catch {
    left: 298px; top: 160px; font-size: 48px; font-weight: 800; color: var(--navy);
    -webkit-text-stroke: 6px var(--white); paint-order: stroke fill;
  }
  .catch-rice {
    left: 386px; top: 270px; font-size: 56px; font-weight: 800; color: var(--red);
    -webkit-text-stroke: 6px var(--white); paint-order: stroke fill;
  }
  .catch-noodle {
    position: absolute; left: 372px; top: 525px; font-size: 165px; font-weight: 800; line-height: 1;
    color: var(--navy); -webkit-text-stroke: 8px var(--white); paint-order: stroke fill;
  }

  .brand-mark {
    position: absolute; left: 560px; top: 36px; width: 56px; height: 56px;
    border-radius: 50%; background: var(--navy);
  }
  .brand-sub { left: 592px; top: 118px; font-size: 24px; font-weight: 600; color: var(--navy); }
  .brand-name { left: 640px; top: 104px; font-size: 96px; font-weight: 800; color: var(--navy); }

  .footer-band { position: absolute; left: 0; top: 905px; width: 849px; height: 295px; background: var(--navy-deep); }
  .store-card {
    position: absolute; left: 14px; top: 922px; width: 482px; height: 264px;
    background: linear-gradient(160deg, #6e5516, #3b2d0b 70%);
    border: 3px solid var(--gold);
    color: var(--gold-light); padding: 20px 22px;
    font-family: "Noto Sans JP", sans-serif;
  }
  .store-card__head { display: flex; align-items: center; gap: 12px; }
  .store-card__dot { width: 32px; height: 32px; border-radius: 50%; background: var(--gold); flex: none; }
  .store-card__name { font-family: "Shippori Mincho B1", serif; font-weight: 800; font-size: 30px; color: var(--gold); }
  .store-card__branch { font-size: 15px; font-weight: 700; margin-top: 8px; color: var(--gold-light); }
  .store-card__addr { font-size: 30px; font-weight: 700; margin-top: 10px; color: var(--white); }
  .store-card__hours { font-size: 20px; font-weight: 700; margin-top: 4px; color: var(--white); }
  .store-card__tel { display: flex; align-items: center; gap: 8px; font-size: 24px; font-weight: 700; margin-top: 8px; color: var(--white); }
  .store-card__tel svg { width: 24px; height: 24px; }

  .coupon {
    position: absolute; left: 512px; top: 918px; width: 325px; height: 264px;
    background: var(--white); border: 3px dashed var(--ink);
    font-family: "Noto Sans JP", sans-serif; text-align: center; padding-top: 14px;
  }
  .coupon__tab { display: inline-block; background: var(--ink); color: var(--white); font-size: 18px; font-weight: 700; padding: 3px 14px; }
  .coupon__amount { font-size: 72px; font-weight: 900; color: var(--ink); line-height: 1.1; letter-spacing: -2px; margin-top: 4px; }
  .coupon__amount small { font-size: 40px; }
  .coupon__type { font-size: 24px; font-weight: 900; color: var(--red); }
  .coupon__shop { font-size: 15px; font-weight: 700; margin-top: 12px; }
  .coupon__limit { font-size: 17px; font-weight: 700; margin-top: 2px; }
</style>
</head>
<body>
<div class="flyer">
  <svg class="backdrop" width="849" height="1200" viewBox="0 0 849 1200">
    <path d="M0 170 C120 130 250 190 320 310 C370 410 350 540 290 620 L0 620 Z" fill="var(--gold)"/>
    <g role="img" aria-label="紺地の和柄模様">
      <path d="M849 540 L849 905 L330 905 L330 720 C420 700 470 620 560 590 C650 560 760 550 849 540 Z" fill="var(--navy)"/>
    </g>
  </svg>

  <div class="dish dish--miso" role="img" aria-label="旨辛味噌をのせたとろみちゃんぽんの写真"></div>
  <div class="dish dish--plain" role="img" aria-label="とろみちゃんぽんの写真"></div>
  <div class="dish dish--mazesoba" role="img" aria-label="台湾風まぜそばの写真"></div>

  <div class="menu-label label-miso"><span class="name">とろみちゃんぽん<br>旨辛味噌のせ</span><span class="price">¥ 910</span></div>
  <div class="menu-label label-plain"><span class="name">とろみちゃんぽん</span><span class="price">¥ 880</span></div>
  <div class="menu-label label-mazesoba"><span class="name">台湾風まぜそば</span><span class="price">¥ 910</span></div>

  <p class="v catch">つるつるもちもち！</p>
  <p class="v catch-rice">おコメの</p>
  <p class="catch-noodle">麺</p>

  <div class="brand-mark"></div>
  <p class="v brand-sub">こむぎ茶屋</p>
  <p class="v brand-name">しずくや</p>

  <div class="footer-band"></div>
  <section class="store-card">
    <div class="store-card__head"><span class="store-card__dot"></span><span class="store-card__name">こむぎ茶屋 しずくや</span></div>
    <p class="store-card__branch">みずほ灯籠館店（道の駅みずほ灯籠館フードコート内）</p>
    <p class="store-card__addr">長岡市桜井町318</p>
    <p class="store-card__hours">（営業時間 10:00 ~ 19:00）</p>
    <p class="store-card__tel">
      <svg viewBox="0 0 24 24"><path d="M6.6 10.8a15 15 0 0 0 6.6 6.6l2.2-2.2a1 1 0 0 1 1-.25 11.4 11.4 0 0 0 3.6.6 1 1 0 0 1 1 1V20a1 1 0 0 1-1 1A17 17 0 0 1 3 4a1 1 0 0 1 1-1h3.5a1 1 0 0 1 1 1c0 1.25.2 2.45.6 3.6a1 1 0 0 1-.25 1z" fill="currentColor"/></svg>
      TEL：090-4213-8062
    </p>
  </section>

  <section class="coupon">
    <span class="coupon__tab">飲食代から</span>
    <p class="coupon__amount"><small>¥</small>100<small>OFF</small></p>
    <p class="coupon__type">Cash Back クーポン</p>
    <p class="coupon__shop">こむぎ茶屋 しずくや</p>
    <p class="coupon__limit">有効期限：2023年2月末</p>
  </section>
</div>
</body>
</html>
```